Company or website name
- Marla Quist Design & Decor
- Passionate about wedding floral design and decor. Events I create are timeless, classic and elegant, customized 100% to the brides’ desires. Inspiring them with a vision of what is possible & asking them to step inside it and see it for themselves

```html
<!DOCTYPE html>
<html lang="en">
<head>
<meta charset="utf-8">
<title>Marla Quist Design &amp; Decor — Stationery</title>
<link rel="stylesheet" href="https://fonts.googleapis.com/css2?family=Josefin+Sans:wght@300;400&display=swap">
<style>
  :root {
    --canvas: #ffffff;
    --paper: #fcf1f1;
    --paper-edge: #ecdcdc;
    --coral: #ef6b6e;
    --coral-soft: #f08a86;
  }
  * { margin: 0; padding: 0; box-sizing: border-box; }
  html, body {
    width: 1040px;
    height: 1200px;
    overflow: hidden;
    background: var(--canvas);
  }
  .stationery {
    position: relative;
    width: 1040px;
    height: 1200px;
    font-family: "Josefin Sans", "Gill Sans", sans-serif;
    font-weight: 300;
    color: var(--coral);
  }

  /* Letterhead */
  .letterhead {
    position: absolute;
    left: 132px;
    top: 36px;
    width: 868px;
    height: 1126px;
    background: var(--paper);
    border: 1px solid var(--paper-edge);
  }
  .letterhead-contact {
    position: absolute;
    right: 26px;
    top: 52px;
    height: 800px;
    writing-mode: vertical-rl;
    transform: rotate(180deg);
    font-size: 17px;
    letter-spacing: 0.3px;
    white-space: nowrap;
    text-align: left;
  }
  .letterhead-brand {
    position: absolute;
    left: 44px;
    top: 856px;
    width: 500px;
  }
  .letterhead-brand .brand-mark {
    display: block;
    width: 146px;
    height: 146px;
    margin-left: 82px;
  }
  .letterhead-brand .brand-name {
    display: block;
    margin-top: 22px;
    font-size: 38px;
    white-space: nowrap;
  }

  /* Business card */
  .business-card {
    position: absolute;
    left: 34px;
    top: 290px;
    width: 206px;
    height: 346px;
    background: var(--paper);
    border: 1px solid var(--paper-edge);
  }
  .card-contact {
    position: absolute;
    right: 22px;
    top: 26px;
    text-align: right;
    font-size: 9.5px;
    line-height: 1.45;
  }
  .card-contact .card-person {
    font-size: 12.5px;
    margin-bottom: 14px;
  }
  .card-brand {
    position: absolute;
    left: 30px;
    top: 236px;
    width: 170px;
  }
  .card-brand .brand-mark {
    display: block;
    width: 58px;
    height: 58px;
    margin-left: 38px;
  }
  .card-brand .brand-name {
    display: block;
    margin-top: 10px;
    font-size: 12.5px;
    white-space: nowrap;
  }
</style>
</head>
<body>
  <main class="stationery">
    <section class="letterhead" aria-label="Letterhead">
      <p class="letterhead-contact">Marla Quist Design &amp; Decor . 48 Orchard Lane . Fairhaven, MA 02719 . 508.555.0147 . hello@marlaquist.com</p>
      <div class="letterhead-brand">
        <svg class="brand-mark" viewBox="0 0 100 100" aria-hidden="true">
          <circle cx="50" cy="50" r="50" fill="var(--coral)"/>
        </svg>
        <span class="brand-name">Marla Quist Design &amp; Decor</span>
      </div>
    </section>

    <section class="business-card" aria-label="Business card">
      <div class="card-contact">
        <p class="card-person">Marla Quist</p>
        <p>48 Orchard Lane</p>
        <p>Fairhaven, MA 02719</p>
        <p>508.555.0147</p>
        <p>hello@marlaquist.com</p>
      </div>
      <div class="card-brand">
        <svg class="brand-mark" viewBox="0 0 100 100" aria-hidden="true">
          <circle cx="50" cy="50" r="50" fill="var(--coral)"/>
        </svg>
        <span class="brand-name">Marla Quist Design &amp; Decor</span>
      </div>
    </section>
  </main>
</body>
</html>
```